Wordpress template for a mens-choire webpage

Task is to design a Wordpress template for an 98 years old estonian mens choire webpage.
Design should involve details from the attached files, choire logo and the colors of the choire flag: in horizontal orientation bright sky-blue, white, bright grass-green.
Designer signature is allowed to be added to the template, with country of origin.

Thank you everyone for your great designs!
Our project has now entered into a voting and decision phase until 14th of March 2014 (included).

```html
<!DOCTYPE html>
<html lang="en">
<head>
<meta charset="utf-8">
<title>Harbor Voices – Men's Choir</title>
<link rel="stylesheet" href="https://fonts.googleapis.com/css2?family=Source+Sans+3:ital,wght@0,400;0,600;0,700;1,400&display=swap">
<style>
:root{
  --parchment:#e6c38c;
  --parchment-light:#eccfa0;
  --parchment-dark:#c9a265;
  --panel:#dfbf88;
  --ink:#3b2f22;
  --ink-soft:#5a4630;
  --heading-green:#4f6b3c;
  --dark-btn:#3c3b37;
  --white:#ffffff;
}
*{box-sizing:border-box;margin:0;padding:0}
html,body{width:800px;height:1200px;overflow:hidden}
body{
  position:relative;
  font-family:"Source Sans 3","Source Sans Pro",Arial,sans-serif;
  color:var(--ink);
  background:radial-gradient(ellipse at 50% 40%,var(--parchment-light),var(--parchment) 60%,var(--parchment-dark));
}
.abs{position:absolute}
.nowrap{white-space:nowrap}
.topbar{left:0;top:0;width:800px;height:30px;background:var(--parchment-dark);display:flex;justify-content:flex-end;align-items:center;gap:18px;padding-right:80px;font-size:11px;color:var(--ink)}
.topbar span{display:flex;align-items:center;gap:6px}
.brand{left:82px;top:60px;display:flex;align-items:center;gap:8px;font-size:17px;font-weight:700;color:var(--ink)}
.brand-dot{width:26px;height:26px;border-radius:50%;background:var(--ink-soft)}
.search{left:583px;top:66px;width:138px;height:18px;background:var(--white)}
.search svg{position:absolute;right:3px;top:2px}
.nav{right:83px;top:103px;display:flex;gap:15px;font-size:14px;line-height:16px;font-weight:700;color:var(--ink);white-space:nowrap}
.nav a{color:inherit;text-decoration:none}
.nav-rule{left:172px;top:128px;width:550px;height:3px;background:var(--ink);border-radius:2px}
.slider{left:115px;top:183px;width:572px;height:207px;background:var(--panel);border-radius:8px;box-shadow:0 2px 6px rgba(80,50,20,.3)}
.arrow{top:257px;width:59px;height:59px;border-radius:50%;background:#c7a06a;display:flex;align-items:center;justify-content:center}
.slide-title{left:140px;top:206px;font-size:17px;line-height:24px;font-weight:700;color:var(--heading-green);text-transform:uppercase;white-space:nowrap}
.slide-text{left:140px;top:289px;font-size:11.5px;line-height:14px;color:var(--ink-soft);white-space:nowrap}
.dots{left:140px;top:340px;display:flex;gap:4px}
.dots i{width:10px;height:10px;border-radius:50%;background:var(--ink)}
.photo-frame{left:394px;top:146px;width:268px;height:223px;background:#efdcb6;border-radius:6px;box-shadow:0 2px 6px rgba(60,40,10,.45);padding:7px 9px}
.photo{border-radius:6px;width:100%;height:100%}
.photo-choir{background:linear-gradient(160deg,#6b3b22,#3e2617 40%,#2a3a7a 70%,#c9c2b2)}
.band{left:33px;width:733px;height:6px;background:var(--ink);border-radius:3px}
.ornament{background:linear-gradient(90deg,transparent,rgba(59,47,34,.55) 15%,rgba(59,47,34,.55) 85%,transparent);border-radius:20px}
h2.section{font-size:16px;font-weight:400;color:var(--ink);white-space:nowrap}
.welcome-text{left:81px;top:528px;width:368px;font-size:8.8px;line-height:11.4px;color:var(--ink)}
.welcome-text p+p{margin-top:9px}
.btn{background:var(--dark-btn);color:var(--white);font-size:9px;display:flex;align-items:center;justify-content:center;border-radius:3px}
.video{left:489px;top:500px;width:232px;height:118px;border-radius:8px;background:linear-gradient(180deg,#1b1a19,#3a342c 60%,#141312);display:flex;align-items:center;justify-content:center}
.blog-img{left:81px;top:688px;width:146px;height:82px;background:linear-gradient(135deg,#5a3a22,#d8c8b0 50%,#8a6a4a)}
.blog-title{left:245px;top:695px;font-size:10.5px;font-weight:700;white-space:nowrap}
.blog-date{left:245px;top:711px;font-size:8px}
.blog-text{left:245px;top:725px;width:305px;font-size:8.2px;line-height:10.6px}
.field{left:575px;width:145px;height:22px;background:var(--white);border-radius:4px;font-size:8px;color:#a9a9a9;padding:6px 8px}
.test-title{left:342px;top:804px;width:120px;text-align:center;font-size:15px}
.test-rule{left:352px;top:826px;width:100px;height:2px;background:var(--ink)}
.test-box{left:268px;top:838px;width:280px;height:100px;background:var(--panel);box-shadow:0 2px 6px rgba(80,50,20,.3);border-radius:3px}
.avatar{left:284px;top:852px;width:42px;height:43px;border:2px solid var(--white);background:linear-gradient(160deg,#7a5a40,#3a2a20)}
.quote{left:342px;top:853px;width:196px;font-size:9px;line-height:11.4px;font-style:italic;color:var(--ink-soft)}
.quote b{display:block;margin-top:9px;font-weight:600}
.big-ornament{left:75px;top:860px;width:650px;height:195px;background:radial-gradient(ellipse at 50% 90%,rgba(59,47,34,.5),rgba(59,47,34,.25) 45%,transparent 70%)}
.foot-col{top:1080px;font-size:9.5px;line-height:11.4px;white-space:nowrap}
.foot-col h3{font-size:12px;font-weight:400;margin-bottom:6px}
.social{top:1108px;display:flex;gap:11px;left:575px}
.social i{width:22px;height:22px;background:var(--ink-soft);border-radius:2px}
.copy{left:0;top:1182px;width:800px;height:18px;background:var(--parchment-dark);font-size:8px;text-align:center;line-height:19px}
</style>
</head>
<body>
<header>
  <div class="abs topbar">
    <span><svg width="11" height="8" viewBox="0 0 11 8"><rect x=".5" y=".5" width="10" height="7" fill="none" stroke="#3b2f22"/><path d="M.5 .5l5 4 5-4" fill="none" stroke="#3b2f22"/></svg>hello@harborvoices.org</span>
    <span><svg width="8" height="13" viewBox="0 0 8 13"><rect x=".5" y=".5" width="7" height="12" rx="1" fill="none" stroke="#3b2f22"/><rect x="2" y="2" width="4" height="7" fill="#3b2f22"/></svg>0800 4417 302</span>
  </div>
  <div class="abs brand"><span class="brand-dot"></span>Harbor Voices</div>
  <div class="abs search"><svg width="14" height="14" viewBox="0 0 14 14"><circle cx="6" cy="6" r="4.5" fill="none" stroke="#222" stroke-width="1.6"/><path d="M9.3 9.3l3.5 3.5" stroke="#222" stroke-width="1.8"/></svg></div>
  <nav class="abs nav">
    <a>HOME</a><a>ABOUT</a><a>BLOG</a><a>GALLERY</a><a>CONTACT</a>
  </nav>
  <div class="abs nav-rule"></div>
</header>

<section class="hero">
  <div class="abs arrow" style="left:81px"><svg width="14" height="20" viewBox="0 0 14 20"><path d="M11 2L3 10l8 8" fill="none" stroke="#fff" stroke-width="3"/></svg></div>
  <div class="abs arrow" style="left:661px"><svg width="14" height="20" viewBox="0 0 14 20"><path d="M3 2l8 8-8 8" fill="none" stroke="#fff" stroke-width="3"/></svg></div>
  <div class="abs slider"></div>
  <h1 class="abs slide-title">Lorem ipsum dolor sit<br>amet consectetuer<br>adipiscing elit</h1>
  <p class="abs slide-text">Sed diam nonummy nibh euismod tincidunt ut<br>laoreet dolore magna aliquam erat volutpat. enim<br>ad minim veniam, quis nostrud exerci tation.</p>
  <div class="abs dots"><i></i><i></i><i></i></div>
  <div class="abs photo-frame"><div class="photo photo-choir" role="img" aria-label="Photo of a robed choir singing in a cathedral"></div></div>
</section>

<div class="abs band" style="top:437px"></div>
<div class="abs ornament" role="img" aria-label="Decorative floral divider" style="left:75px;top:450px;width:645px;height:32px"></div>

<section class="welcome">
  <h2 class="abs section" style="left:81px;top:499px">Welcome to our site</h2>
  <div class="abs welcome-text">
    <p>Lorem ipsum dolor sit amet, consectetuer adipiscing elit, sed diam nonummy nibh euismod tincidunt ut laoreet dolore magna aliquam erat volutpat. Ut wisi enim ad minim veniam, quis nostrud exerci tation ullamcorper suscipit lobortis nisl ut aliquip ex ea commodo consequat. Duis autem vel eum iriure dolor in hendrerit in vulputate.</p>
    <p>Lorem ipsum dolor sit amet, consectetuer adipiscing elit, sed diam nonummy nibh euismod tincidunt ut laoreet dolore.</p>
  </div>
  <a class="abs btn" style="left:81px;top:616px;width:72px;height:24px">Read More</a>
  <div class="abs video" role="img" aria-label="Video of a men's choir performing on stage">
    <svg width="44" height="44" viewBox="0 0 44 44"><circle cx="22" cy="22" r="20" fill="none" stroke="#fff" stroke-width="2"/><path d="M17 12l14 10-14 10z" fill="#fff"/></svg>
  </div>
</section>

<section class="blog">
  <h2 class="abs section" style="left:81px;top:661px;font-size:15px">Recent Blog Posts</h2>
  <div class="abs blog-img" role="img" aria-label="Group photo of choir members"></div>
  <h3 class="abs blog-title">Duis autem vel eum iriure dolor in hendrerit</h3>
  <div class="abs blog-date">Feb 27, 2014</div>
  <p class="abs blog-text">Vulputate velit esse molestie consequat, vel illum dolore eu feugiat nulla facilisis at vero eros et accumsan et iusto odio dignissim qui blandit Duis autem vel eum iriure dolor in hendrerit in vulputate velit esse molestie consequat, vel illum dolore eu feugiat nulla facilisis at vero eros et aan et iusto...<b class="nowrap">READ MORE</b></p>
</section>

<section class="newsletter">
  <h2 class="abs section" style="left:575px;top:662px;font-size:14.5px">Sign Up for Newsletters</h2>
  <div class="abs field" style="top:689px">Full Name</div>
  <div class="abs field" style="top:715px">Email Address</div>
  <a class="abs btn" style="left:575px;top:749px;width:57px;height:20px">Submit</a>
</section>

<div class="abs big-ornament" role="img" aria-label="Large folk floral ornament with founding year 1916"></div>

<section class="testimonials">
  <h2 class="abs section test-title">Testimonials</h2>
  <div class="abs test-rule"></div>
  <div class="abs test-box"></div>
  <div class="abs avatar" role="img" aria-label="Portrait of the reviewer"></div>
  <p class="abs quote">Duis autem vel eum iriure dolor in hendrerit in vulputate velit esse molestie consequat, vel illum dolore eu feugiat nulla facilisis at vero eros et accumsan et iusto.<b>Martin - Lorem Ipsum</b></p>
</section>

<div class="abs band" style="top:1058px;height:12px;border-radius:4px"></div>

<footer>
  <div class="abs foot-col" style="left:81px"><h3>Quick links</h3>Home<br>About<br>Blog<br>Gallery<br>Videos<br>Contact</div>
  <div class="abs foot-col" style="left:214px"><h3>Support us</h3>Home<br>About<br>Blog<br>Gallery<br>Videos<br>Contact</div>
  <div class="abs foot-col" style="left:357px"><h3>Contact us</h3>12 Linden Court, Harbor Row<br>48, 20915 Eastport<br>Phone: 0800 4417 390<br>Email: hello@harborvoices.org</div>
  <div class="abs foot-col" style="left:575px"><h3>Connect with us</h3></div>
  <div class="abs social"><i></i><i></i><i></i><i></i></div>
  <div class="abs copy">Copyright © 2014 Harbor Voices Choir.</div>
</footer>
</body>
</html>
```